Velmar Ops Business Cards

We need to design some upbeat business cards. We are an Industrial Rope Access Company/Height Safety Company that specialize in Rope Access, Confined Space, Anchor Points, Safety Systems, PPE Inspecions and Rigging.
Company name is Velmar Ops Ltd
Card is for Gareth Lomas the Company Director
His mobile number is 027 418 9072 and email is gareth@velmarops.co.nz. Website address is www.velmarops.co.nz.
We will post some pictures below to ensure you get a good idea of what we do.

```html
<!DOCTYPE html>
<html lang="en">
<head>
<meta charset="utf-8">
<title>Velmar Ops Business Cards</title>
<link rel="stylesheet" href="https://fonts.googleapis.com/css2?family=Saira:wght@700&family=Saira+Condensed:wght@500;600&family=Work+Sans:wght@400;500&display=swap">
<style>
  :root {
    --backdrop: #1d1d20;
    --card-navy: #24205f;
    --card-navy-deep: #1f1b54;
    --emboss-navy: #1a174a;
    --emboss-light: rgba(120, 112, 200, 0.28);
    --silver: #d3d3df;
    --silver-soft: #b9b9ca;
  }
  * { margin: 0; padding: 0; box-sizing: border-box; }
  html, body {
    width: 1200px;
    height: 900px;
    overflow: hidden;
    background: var(--backdrop);
  }
  .card-set {
    position: relative;
    width: 1200px;
    height: 900px;
    display: flex;
    flex-direction: column;
    align-items: center;
    justify-content: center;
    gap: 36px;
  }
  .card {
    position: relative;
    width: 660px;
    height: 377px;
    background: linear-gradient(160deg, var(--card-navy) 0%, var(--card-navy-deep) 100%);
    box-shadow: 0 14px 30px rgba(0, 0, 0, 0.45);
  }

  /* Front */
  .card-front .brand-name {
    position: absolute;
    left: 0;
    right: 0;
    top: 118px;
    text-align: center;
    font-family: "Saira", sans-serif;
    font-weight: 700;
    font-size: 64px;
    letter-spacing: 1px;
    color: var(--silver);
    line-height: 1;
  }
  .card-front .services {
    position: absolute;
    left: 0;
    right: 0;
    top: 232px;
    text-align: center;
    font-family: "Work Sans", sans-serif;
    font-weight: 500;
    font-size: 15px;
    letter-spacing: 0.6px;
    line-height: 1.35;
    color: var(--silver-soft);
    text-transform: uppercase;
  }

  /* Back */
  .card-back .person {
    position: absolute;
    right: 400px;
    top: 150px;
    text-align: right;
  }
  .card-back .person-name {
    font-family: "Saira Condensed", sans-serif;
    font-weight: 600;
    font-size: 42px;
    line-height: 1;
    color: var(--emboss-navy);
    text-shadow: 1px 1px 0 var(--emboss-light), -1px -1px 0 rgba(0, 0, 0, 0.25);
  }
  .card-back .person-role {
    font-family: "Work Sans", sans-serif;
    font-weight: 500;
    font-size: 17px;
    letter-spacing: 0.5px;
    color: var(--emboss-navy);
    text-shadow: 1px 1px 0 var(--emboss-light);
    margin-top: 2px;
  }
  .card-back .divider {
    position: absolute;
    left: 278px;
    top: 144px;
    width: 2px;
    height: 82px;
    background: var(--emboss-navy);
    box-shadow: 1px 0 0 var(--emboss-light);
  }
  .card-back .contact-list {
    position: absolute;
    left: 300px;
    top: 146px;
    list-style: none;
  }
  .card-back .contact-list li {
    display: flex;
    align-items: center;
    gap: 12px;
    height: 27px;
    font-family: "Work Sans", sans-serif;
    font-weight: 400;
    font-size: 20px;
    letter-spacing: 0.4px;
    color: var(--silver);
  }
  .card-back .contact-icon {
    width: 13px;
    height: 13px;
    flex: none;
  }
</style>
</head>
<body>
<main class="card-set">
  <section class="card card-front" aria-label="Card front">
    <div class="brand-name">Velmar Ops</div>
    <p class="services">
      Rope Access - Confined Space - Anchor Points<br>
      Safety Systems - PPE Inspecions - Rigging.
    </p>
  </section>

  <section class="card card-back" aria-label="Card back">
    <div class="person">
      <div class="person-name">Gareth Lomas</div>
      <div class="person-role">Director</div>
    </div>
    <div class="divider"></div>
    <ul class="contact-list">
      <li>
        <svg class="contact-icon" viewBox="0 0 16 16" aria-hidden="true">
          <path d="M3.5 1.5l2.5 0 1 3.5-1.8 1.2c.8 1.8 2.2 3.2 4 4l1.2-1.8 3.5 1v2.5c0 .8-.7 1.5-1.5 1.5C6.6 13.4 2.6 9.4 2 3c0-.8.7-1.5 1.5-1.5z" fill="#d3d3df"/>
        </svg>
        027 418 9072
      </li>
      <li>
        <svg class="contact-icon" viewBox="0 0 16 16" aria-hidden="true">
          <rect x="1.5" y="3.5" width="13" height="9" fill="none" stroke="#d3d3df" stroke-width="1.5"/>
          <path d="M1.5 3.5L8 9l6.5-5.5" fill="none" stroke="#d3d3df" stroke-width="1.5"/>
        </svg>
        gareth@velmarops.co.nz
      </li>
      <li>
        <svg class="contact-icon" viewBox="0 0 16 16" aria-hidden="true">
          <circle cx="8" cy="8" r="6.3" fill="none" stroke="#d3d3df" stroke-width="1.3"/>
          <ellipse cx="8" cy="8" rx="2.8" ry="6.3" fill="none" stroke="#d3d3df" stroke-width="1.1"/>
          <path d="M1.7 8h12.6M2.8 4.8h10.4M2.8 11.2h10.4" stroke="#d3d3df" stroke-width="1"/>
        </svg>
        www.velmarops.co.nz
      </li>
    </ul>
  </section>
</main>
</body>
</html>
```